Rising Paths Web Design

I am starting a new company that will provide LIFE COACHING services - I have tried to design a website, but it's too complicated. Right now, it's just me - I'm the only person that will provide services through the website - I have used artmarket to purchase a logo (see below). I want to be able to update the website myself, but need a template - basic design. Because I am not technologically savvy enough to explain in words - I basically want to have a website that will provide basic information about my services (coaching), a page about me and my background, hopefully scheduling possibilities, and testimonials — also a page for writing/blogs. I bought a website through NetHarbor - so when I have a template, I guess I”d use that - but maybe I’ll need to work with a designer to actually get it up on the internet. I have a head shot that I’ll upload, too.
Target Market(s)
Clients from the independent (private school) world - teachers, administrators
Number of Pages Required
4 page
Look and feel
Each slider illustrates characteristics of the customer's brand and the style your logo design should communicate.

```html
<!DOCTYPE html>
<html lang="en">
<head>
<meta charset="utf-8">
<title>Rising Paths Coaching</title>
<link href="https://fonts.googleapis.com/css2?family=Marcellus&family=Barlow:wght@400;500;600;700&display=swap" rel="stylesheet">
<style>
:root{
  --teal:#12b3a0;
  --teal-dark:#0a9c8c;
  --teal-soft:#d7efec;
  --mist:#eef7f6;
  --ink:#2b2b2b;
  --grey:#555;
  --white:#fff;
}
*{box-sizing:border-box;margin:0;padding:0}
html,body{width:1200px;height:4383px;overflow:hidden}
body{position:relative;background:var(--white);font-family:'Barlow',sans-serif;color:var(--ink)}
.abs{position:absolute}
.serif{font-family:'Marcellus',serif}
.eyebrow{font-size:18px;letter-spacing:1px;color:var(--teal);text-transform:uppercase}
.title{font-family:'Marcellus',serif;font-size:40px;letter-spacing:2px;text-transform:uppercase;color:var(--ink)}
.rule{height:2px;width:90px;background:var(--teal)}
.center{text-align:center;left:0;width:1200px}
.btn{display:flex;align-items:center;justify-content:center;border-radius:30px;font-weight:700;letter-spacing:1.5px;text-transform:uppercase;font-size:15px}
.btn-solid{background:var(--teal);color:var(--white)}
.btn-line{border:2px solid var(--teal);color:var(--teal);background:var(--white)}

/* brand name */
.brand{display:flex;align-items:center;gap:10px;font-family:'Barlow',sans-serif;font-weight:600;font-size:21px;color:#3a3a3a;white-space:nowrap}
.brand-dot{width:16px;height:16px;border-radius:50%;background:var(--teal);flex:none}

/* header */
.nav{top:0;left:0;width:1200px;height:82px;background:var(--white);z-index:3}
.nav a{position:absolute;top:38px;font-size:15px;color:var(--ink);text-decoration:none;text-transform:uppercase}
.nav .active::after{content:"";position:absolute;left:0;right:0;top:33px;height:3px;background:var(--teal)}
.nav .cta{top:26px;left:900px;width:216px;height:42px;border-radius:22px;background:var(--teal);color:var(--white);display:flex;align-items:center;justify-content:center;font-size:14px}
.nav .brand{position:absolute;left:100px;top:34px}

/* hero */
.hero{top:82px;left:0;width:1200px;height:690px;background:linear-gradient(90deg,#c8a37f 0%,#efe6dc 35%,#f6f1ea 55%,#cdb9a8 80%,#a98f7c 100%)}
.hero-welcome{top:264px;font-size:28px;color:#555;letter-spacing:2px;font-family:'Marcellus',serif}
.hero-name{top:296px;font-size:60px;color:#444;font-family:'Marcellus',serif;letter-spacing:1px}
.hero-sub{top:356px;font-size:30px;color:var(--teal);letter-spacing:9px;font-family:'Marcellus',serif}

/* about */
.portrait{left:110px;top:860px;width:410px;height:410px;border-radius:50%;background:radial-gradient(circle at 50% 55%,#d9c4a8 0 38%,var(--teal-soft) 39%)}
.about-text{left:598px;top:1021px;width:500px;font-size:18px;line-height:31px;color:#444}

/* services */
.svc-head{font-weight:700;font-size:17px;letter-spacing:1px;text-transform:uppercase;color:#333}
.svc-text{font-size:13.5px;line-height:18.5px;color:#555}
.icon-ring{width:88px;height:88px;border-radius:50%;border:2px solid var(--teal);background:var(--white);display:flex;align-items:center;justify-content:center}

/* blogs */
.blog-img{height:212px;width:320px;border-top-right-radius:34px}
.blog-card{width:296px;height:218px;border:2px solid var(--teal);border-top-left-radius:28px;background:var(--white);padding:16px 22px}
.blog-card.feature{background:var(--teal);color:var(--white)}
.blog-date{font-size:13px;font-weight:600}
.blog-title{font-size:18.5px;font-weight:600;line-height:23px;margin-top:10px}
.blog-ex{font-size:13px;line-height:18px;margin-top:6px;color:#555}
.feature .blog-ex{color:#e6fbf8}
.blog-btn{margin-top:14px;width:132px;height:36px;font-size:11px}

/* testimonials */
.testi{top:2837px;left:0;width:1200px;height:590px;background:linear-gradient(180deg,#19b4a2 0%,#3cc0b0 60%,#6ccbbe 100%)}
.quote-box{left:221px;top:3050px;width:741px;height:260px;border:2px solid var(--white);border-radius:60px 0 60px 0}
.quote-text{top:3130px;font-size:19px;line-height:31px;color:var(--white)}

/* appointment */
.appt{top:3421px;left:0;width:1200px;height:620px;background:linear-gradient(90deg,#f7f3ee 0%,#f1e3d3 40%,#d9a98a 70%,#9c8578 100%)}
.field{background:var(--white);border:1px solid #bbb;font-size:14px;color:#777;padding:12px 14px}

/* footer */
.foot-head{font-weight:700;font-size:14px;letter-spacing:1px;color:#333;text-transform:uppercase}
.foot-list{font-size:14px;line-height:25px;color:#444;list-style:none}
.foot-div{width:2px;height:160px;background:var(--teal)}
.copy{top:4323px;left:0;width:1200px;height:60px;background:var(--mist);display:flex;align-items:center;justify-content:center;font-size:13px;color:#666}
</style>
</head>
<body>

<!-- header -->
<header class="abs nav">
  <div class="brand"><span class="brand-dot"></span>Rising Paths Coaching</div>
  <a class="active" style="left:344px">About Us</a>
  <a style="left:460px">Services</a>
  <a style="left:572px">Blogs</a>
  <a style="left:666px">Testimonial</a>
  <a style="left:802px">Contact</a>
  <a class="cta">Schedule Appointment</a>
</header>

<!-- hero -->
<section class="abs hero" role="img" aria-label="Photo of a coach in conversation with a smiling client"></section>
<div class="abs center hero-welcome">WELCOME TO</div>
<div class="abs center hero-name">RISING PATHS</div>
<div class="abs center hero-sub">COACHING</div>
<div class="abs btn btn-solid" style="left:520px;top:432px;width:178px;height:48px">Learn More</div>
<svg class="abs" style="left:0;top:640px" width="1200" height="150" viewBox="0 0 1200 150">
  <path d="M0 40 C300 140 700 140 1200 40 L1200 150 L0 150 Z" fill="#fff"/>
  <path d="M0 40 C300 140 700 140 1200 40" fill="none" stroke="var(--teal)" stroke-width="6"/>
  <path d="M600 32 v22 M592 46 l8 8 8-8" stroke="#888" stroke-width="2" fill="none"/>
</svg>

<!-- about -->
<svg class="abs" style="left:90px;top:840px" width="460" height="480" viewBox="0 0 460 480">
  <circle cx="225" cy="225" r="203" fill="none" stroke="var(--teal)" stroke-width="2"/>
  <path d="M395 100 A205 205 0 0 1 260 465" fill="none" stroke="var(--teal)" stroke-width="2"/>
</svg>
<div class="abs portrait" role="img" aria-label="Head shot of the coach"></div>
<div class="abs eyebrow" style="left:600px;top:904px;font-size:20px">About Me</div>
<div class="abs title" style="left:598px;top:928px;font-size:44px">Clara Whitfield</div>
<div class="abs rule" style="left:600px;top:980px"></div>
<p class="abs about-text">Clara has over 35 years experience teaching and leading in independent schools, including eleven as Head of School. Her coaching practice focuses on independent schools, supporting teachers, administrators, Board members, and parents as they navigate their own Rising Paths.</p>
<div class="abs btn btn-line" style="left:600px;top:1192px;width:180px;height:48px">Learn More</div>

<!-- services -->
<svg class="abs" style="left:0;top:1380px" width="1200" height="760" viewBox="0 0 1200 760">
  <defs><linearGradient id="svcbg" x1="0" y1="0" x2="0" y2="1"><stop offset="0" stop-color="#eaf6f4"/><stop offset="1" stop-color="#d7efeb"/></linearGradient></defs>
  <path d="M0 120 C250 20 500 0 700 10 C900 20 1080 70 1200 110 L1200 730 C900 700 300 700 0 735 Z" fill="url(#svcbg)"/>
  <path d="M700 10 C900 20 1080 70 1200 110" fill="none" stroke="var(--teal)" stroke-width="6"/>
</svg>
<div class="abs center eyebrow" style="top:1459px">What We Offer</div>
<div class="abs center title" style="top:1482px">Coaching Service</div>
<div class="abs rule" style="left:555px;top:1534px"></div>

<div class="abs icon-ring" style="left:564px;top:1570px"><svg width="40" height="40" viewBox="0 0 40 40" fill="none" stroke="#12b3a0" stroke-width="2"><circle cx="13" cy="14" r="5"/><circle cx="27" cy="14" r="5"/><path d="M5 34c0-7 4-11 8-11s8 4 8 11M19 34c0-7 4-11 8-11s8 4 8 11"/></svg></div>
<div class="abs center svc-head" style="top:1667px">Guiding With Professionalism</div>
<p class="abs svc-text" style="left:408px;top:1692px;width:390px;text-align:center">I help you re-imagine your life. With extensive experience as a certified professional coach and over thirty years of teaching and leadership experience, my individualized approach will help you attain your goals.</p>

<div class="abs icon-ring" style="left:293px;top:1782px"><svg width="40" height="40" viewBox="0 0 40 40" fill="none" stroke="#12b3a0" stroke-width="2"><path d="M20 4v26M12 12l8-8 8 8M10 36h20M14 30h12"/></svg></div>
<div class="abs svc-head" style="left:104px;top:1879px;width:286px;text-align:right">Growing Your Goals</div>
<p class="abs svc-text" style="left:104px;top:1904px;width:286px;text-align:right">I help you re-imagine your life. With extensive experience as a certified professional coach and over thirty years of teaching and leadership experience, my individualized approach will help you attain your goals.</p>

<div class="abs icon-ring" style="left:822px;top:1782px"><svg width="40" height="40" viewBox="0 0 40 40" fill="none" stroke="#12b3a0" stroke-width="2"><circle cx="20" cy="22" r="11"/><circle cx="20" cy="22" r="4"/><circle cx="32" cy="8" r="4"/></svg></div>
<div class="abs svc-head" style="left:833px;top:1879px;width:290px">Giving You Voice</div>
<p class="abs svc-text" style="left:833px;top:1904px;width:276px">Committing to new choices and opportunities is just that – a commitment, and it's a big one that will take a lot a dedication. My commitment is to hear you and support with accountability, understanding and encouragement.</p>

<svg class="abs" style="left:410px;top:1785px" width="396" height="396" viewBox="0 0 396 396">
  <circle cx="198" cy="198" r="190" fill="#fff" stroke="var(--teal)" stroke-width="2"/>
  <circle cx="198" cy="8" r="6" fill="#fff" stroke="var(--teal)" stroke-width="2"/>
  <circle cx="22" cy="138" r="6" fill="#fff" stroke="var(--teal)" stroke-width="2"/>
  <circle cx="376" cy="138" r="6" fill="#fff" stroke="var(--teal)" stroke-width="2"/>
</svg>
<div class="abs" role="img" aria-label="Teal-toned landscape photo of a path through fields" style="left:446px;top:1821px;width:324px;height:324px;border-radius:50%;background:radial-gradient(circle at 50% 40%,#3cc4b2,#10a595 70%,#0d8f80)"></div>
<div class="abs" style="left:446px;top:1966px;width:324px;text-align:center;color:#fff;font-family:'Barlow',sans-serif;font-weight:600;font-size:24px">Rising Paths Coaching</div>

<!-- blogs -->
<div class="abs center eyebrow" style="top:2228px">Recent Posts</div>
<div class="abs center title" style="top:2251px">Latest Blogs</div>
<div class="abs rule" style="left:555px;top:2303px"></div>

<div class="abs blog-img" role="img" aria-label="Photo of a coach at a desk" style="left:107px;top:2345px;background:linear-gradient(135deg,#dfe3e6,#bfc7cc 60%,#a9aeb1)"></div>
<div class="abs blog-card" style="left:120px;top:2536px">
  <div class="blog-date">▦ 25 June 2022</div>
  <div class="blog-title">Sed ut perspiciatis unde omnis iste natus error</div>
  <div class="blog-ex">Lorem ipsum dolor sit amet cons ecte tur adipiscing dolor sit amet cons</div>
  <div class="btn btn-line blog-btn">Learn More</div>
</div>
<div class="abs blog-img" role="img" aria-label="Photo of two women in conversation" style="left:449px;top:2345px;background:linear-gradient(135deg,#f2f0ee,#d9cfc6 60%,#8c7a6c)"></div>
<div class="abs blog-card feature" style="left:459px;top:2536px">
  <div class="blog-date">▦ 25 June 2022</div>
  <div class="blog-title">Sed ut perspiciatis unde omnis iste natus error</div>
  <div class="blog-ex">Lorem ipsum dolor sit amet cons ecte tur adipiscing dolor sit amet cons</div>
  <div class="btn blog-btn" style="background:#fff;color:var(--teal)">Learn More</div>
</div>
<div class="abs blog-img" role="img" aria-label="Photo of two women talking on a staircase" style="left:790px;top:2345px;background:linear-gradient(135deg,#b9c6cf,#dfe4e8 50%,#c19a86)"></div>
<div class="abs blog-card" style="left:802px;top:2536px">
  <div class="blog-date">▦ 25 June 2022</div>
  <div class="blog-title">Sed ut perspiciatis unde omnis iste natus error</div>
  <div class="blog-ex">Lorem ipsum dolor sit amet cons ecte tur adipiscing dolor sit amet cons</div>
  <div class="btn btn-line blog-btn">Learn More</div>
</div>

<!-- testimonials -->
<section class="abs testi" role="img" aria-label="Teal-tinted misty mountain backdrop"></section>
<div class="abs center eyebrow" style="top:2899px;color:#fff">What People Say</div>
<div class="abs center title" style="top:2921px;color:#fff">Testimonials</div>
<div class="abs rule" style="left:555px;top:2973px;background:#fff"></div>
<div class="abs quote-box"></div>
<div class="abs" role="img" aria-label="Client portrait" style="left:483px;top:3015px;width:46px;height:46px;border-radius:50%;border:3px solid #fff;background:#c9c2bb"></div>
<div class="abs" role="img" aria-label="Client portrait" style="left:553px;top:3013px;width:92px;height:92px;border-radius:50%;border:4px solid #fff;background:radial-gradient(circle,#a7d9d2 0 60%,#fff 61% 66%,#12b3a0 67%)"></div>
<div class="abs" role="img" aria-label="Client portrait" style="left:669px;top:3015px;width:46px;height:46px;border-radius:50%;border:3px solid #fff;background:#8e8580"></div>
<div class="abs serif" style="left:250px;top:3100px;font-size:70px;color:#fff;line-height:1">“</div>
<div class="abs center quote-text">Lorem ipsum dolor sit amet consectetur adipiscing elit, sed do eiusmod<br>tempor incididunt ut labore et dolore magna aliqua. Ut enim ad minim veniam,<br>quis nostrud exercitation ullamco laboris nisi ut aliquip</div>
<div class="abs serif" style="left:845px;top:3180px;font-size:70px;color:#fff;line-height:1">”</div>
<div class="abs center" style="top:3234px;font-size:19px;font-weight:700;color:#fff">Daniel Hart</div>
<svg class="abs" style="left:95px;top:3110px" width="30" height="46" viewBox="0 0 30 46"><path d="M24 4 6 23l18 19" fill="none" stroke="#fff" stroke-width="3"/></svg>
<svg class="abs" style="left:1080px;top:3110px" width="30" height="46" viewBox="0 0 30 46"><path d="M6 4l18 19L6 42" fill="none" stroke="#fff" stroke-width="3"/></svg>

<!-- appointment -->
<section class="abs appt" role="img" aria-label="Photo of a woman sitting on a rock watching a mountain sunset"></section>
<svg class="abs" style="left:0;top:3345px" width="1200" height="110" viewBox="0 0 1200 110">
  <path d="M0 78 C300 100 500 60 760 70 C950 78 1100 40 1200 30 L1200 110 L0 110 Z" fill="#f7f3ee"/>
  <path d="M0 78 C300 100 500 60 760 70 C950 78 1100 40 1200 30" fill="none" stroke="#fff" stroke-width="2" stroke-dasharray="8 6"/>
  <circle cx="802" cy="60" r="44" fill="none" stroke="#fff" stroke-width="2" stroke-dasharray="8 6"/>
</svg>
<div class="abs eyebrow" style="left:124px;top:3540px;font-size:16px">Book Apointment Now</div>
<div class="abs title" style="left:124px;top:3562px;font-size:34px">Schedule An Appointment</div>
<div class="abs field" style="left:124px;top:3642px;width:226px;height:44px">Name</div>
<div class="abs field" style="left:356px;top:3642px;width:226px;height:44px">Email address</div>
<div class="abs field" style="left:124px;top:3693px;width:226px;height:44px">Phone</div>
<div class="abs field" style="left:356px;top:3693px;width:226px;height:44px">▦ Select Date</div>
<div class="abs field" style="left:124px;top:3746px;width:458px;height:82px">Message</div>
<div class="abs btn btn-solid" style="left:124px;top:3845px;width:180px;height:48px">Book Now</div>
<svg class="abs" style="left:0;top:3990px" width="1200" height="60" viewBox="0 0 1200 60">
  <path d="M0 30 C200 10 400 40 600 25 C800 10 1000 40 1200 20 L1200 60 L0 60 Z" fill="#fff"/>
</svg>

<!-- footer -->
<div class="abs brand" style="left:96px;top:4170px;font-size:20px"><span class="brand-dot"></span>Rising Paths Coaching</div>

<div class="abs foot-div" style="left:367px;top:4085px"></div>
<div class="abs foot-head" style="left:391px;top:4094px">Navigation</div>
<ul class="abs foot-list" style="left:391px;top:4120px">
  <li>» About Us</li><li>» Services</li><li>» Testimonials</li><li>» Blogs</li><li>» Contact Us</li>
</ul>

<div class="abs foot-div" style="left:576px;top:4085px"></div>
<div class="abs foot-head" style="left:598px;top:4094px">Contact Us</div>
<svg class="abs" style="left:598px;top:4134px" width="24" height="24" viewBox="0 0 24 24"><circle cx="12" cy="12" r="12" fill="var(--teal)"/><path d="M12 5a4 4 0 0 0-4 4c0 3 4 9 4 9s4-6 4-9a4 4 0 0 0-4-4z" fill="#fff"/><circle cx="12" cy="9" r="1.5" fill="var(--teal)"/></svg>
<div class="abs" style="left:632px;top:4128px;font-size:14px;line-height:20px;color:#444">128 Maple Lane, Suite #40<br>Brookfield, VT 05036</div>
<svg class="abs" style="left:598px;top:4190px" width="24" height="24" viewBox="0 0 24 24"><circle cx="12" cy="12" r="12" fill="var(--teal)"/><path d="M8 6l3 3-1.5 2c1 2 2 3 3.5 3.5L15 13l3 3-2 2c-5 0-10-5-10-10z" fill="#fff"/></svg>
<div class="abs" style="left:632px;top:4192px;font-size:14px;color:#444">(555) 201-3388</div>

<div class="abs foot-div" style="left:818px;top:4085px"></div>
<div class="abs foot-head" style="left:840px;top:4094px">Follow Us</div>
<div class="abs" aria-label="Social link" style="left:840px;top:4128px;width:34px;height:34px;border-radius:50%;background:var(--teal)"></div>
<div class="abs" aria-label="Social link" style="left:880px;top:4128px;width:34px;height:34px;border-radius:50%;background:var(--teal)"></div>
<div class="abs" aria-label="Social link" style="left:920px;top:4128px;width:34px;height:34px;border-radius:50%;background:var(--teal)"></div>
<div class="abs" aria-label="Social link" style="left:960px;top:4128px;width:34px;height:34px;border-radius:50%;background:var(--teal)"></div>
<div class="abs" aria-label="Certification badge" style="left:853px;top:4196px;width:70px;height:70px;border-radius:50%;border:3px solid #1b8fb8;background:#fff"></div>
<div class="abs" aria-label="Certification badge" style="left:951px;top:4198px;width:66px;height:66px;background:#1d5c80"></div>
<div class="abs" aria-label="Certification badge" style="left:1045px;top:4198px;width:66px;height:66px;border:2px solid #1b8fb8;background:#fff"></div>

<div class="abs copy">© 2022 Rising Paths Coaching All Rights Reserved</div>

</body>
</html>
```